Flyer, poster, banner and social media titles designs for Community Renewal Guidlines

The Shared Guidelines for Community Renewal provide a nationally agreed framework to guide recovery policy and practice across Australia. The Principles support recovery practitioners, governments, non-government organisations and communities to deliver effective, community-centred recovery outcomes.
The Principles have recently been refreshed through extensive consultation and we require a contemporary visual identity and design suite that will increase awareness, engagement and practical application of the Principles.
The redesign will cover:
• A4 Brochure (primary publication)
• A3 Poster
• Pull up banner
• Social Media Tiles
The new design should:
• Create a recognisable brand for the Shared Guidelines.
• Appeal to both experienced and emerging recovery practitioners.
• Reflect contemporary disaster recovery practice.
• Feel people-focused rather than government-focused.
• Support future resources such as videos, implementation guides, presentations and workshop materials.
• Remain relevant for several years without requiring a major redesign.
Target Audience
• Disaster recovery practitioners
• Government agencies
• Non-government organisations
• Community recovery workers
• Recovery managers and leaders
• Community stakeholders and volunteers
The visual identity should reflect the six Principles:
• Understanding Context
• Recognising Complexity
• Community-Centred Approaches
• Coordination
• Communication
• Capacity Building
The design should communicate:
• Recovery is centred on people and communities.
• Recovery is collaborative and involves many sectors.
• Recovery is adaptive, inclusive and evidence-informed.
• Recovery supports resilience and long-term wellbeing.
• The Principles provide practical guidance for recovery practice.
We are looking for:
• Modern and professional
• Warm and approachable
• Human-centred
• Inclusive and accessible
• Australian in context
• Visually engaging
• Suitable for print and digital use
We would like to avoid:
• Images of disaster destruction
• Emergency response imagery (fire trucks, flashing lights, etc.)
• Overly corporate or bureaucratic designs
• Designs that focus on deficits rather than recovery and growth
Consider themes such as:
• Connection and collaboration
• Communities and people
• Growth, recovery and renewal
Accessibility
Designs should:
• Meet accessibility best practice
• Use clear typography
• Achieve strong colour contrast
• Be suitable for both digital and print formats

Deliverables
1. Principles Brochure
• A4 trifold size x 2 (online and print friendly version)
• A side to include cover side, logos side and overview of principles.
• B side full details of the principles
• Graphic to highlight the 3 c’s concept (RECOVERY Context, complexity, community centred, coordinate, communicate and capacity). Currently 3 circles.
• Can be printed and distributed electronically
2. Poster
• A1 and A3 versions
• Suitable for office and workshop display
3. Pull-Up Banner - 850 mm (W) × 2000 mm (H)
• Conference and event use
• High visual impact
• Strong branding and concise messaging
4. Social Media Tiles x 3
Updates

We are providing an extension and increasing the budget following feedback from designers. We are wanting the resources to look and feel different from the existing designs, considering either a different colour palette in the designs or different motif with the leave design. Any nature based designs should consider the Australian fauna or flora. Also suggest avoiding images in the designs. The principles are not numbered or liner in the concept of how they function. Happy to answer any further questions and thank you for your suggested concepts.

Target Market(s)

Disaster recovery practitioners, Government agencies , Non-government organisations, Community recovery workers and Community stakeholders and volunteers

Industry/Entity Type

Disaster recovery

Colors

Designer to choose colors to be used in the design.

Requirements
Must have
• Modern, warm, visually engaging, human-centred, Australian in context and different to the current design.
Nice to have
• Symbols for each principles
Should not have
• Images of disaster destruction, Emergency response imagery, Overly corporate or bureaucratic designs, Designs that focus on deficits rather than recovery and growth, avoid too much black

```html
<!DOCTYPE html>
<html lang="en">
<head>
<meta charset="utf-8">
<title>Shared Guidelines for Community Renewal – Brochure</title>
<link href="https://fonts.googleapis.com/css2?family=Poppins:wght@400;500;600&family=DM+Serif+Display&display=swap" rel="stylesheet">
<style>
:root{
  --night:#1d3b3d;
  --night-soft:#2a4d4f;
  --gum:#2f6b62;
  --ochre:#e9a23b;
  --ochre-deep:#a8561a;
  --sand:#efe6d6;
  --white:#ffffff;
  --ink:#243233;
  --plain-mark:#b9ab93;
}
*{box-sizing:border-box;margin:0;padding:0}
html,body{width:779px;height:1200px;overflow:hidden;background:var(--white)}
body{position:relative;font-family:"Poppins",sans-serif;color:var(--white)}
.spread{position:absolute;left:37px;width:704px;height:541px;display:flex}
.spread--outside{top:40px}
.spread--inside{top:609px}
.panel{position:relative;width:234.6px;height:100%;overflow:hidden}
.panel--night{background:var(--night)}
.panel--sand{background:var(--sand);color:var(--ink)}
.accent{color:var(--ochre)}
.serif{font-family:"DM Serif Display",serif;font-weight:400;line-height:.85}

/* intro panel */
.intro{padding:18px 11px 0 13.5px}
.eyebrow{font-size:6.2px;letter-spacing:.3px;text-transform:uppercase}
.intro .title{margin:6px 0 0 20px;font-size:19px}
.intro .title-big{margin:-3px 0 0 1px;font-size:30px;color:var(--ochre)}
.intro p{font-size:6.3px;line-height:9.6px;font-weight:400;margin-top:4px}
.intro .subhead{font-size:6.2px;color:var(--ochre);margin-top:5px;font-weight:500}
.sprig{position:absolute;left:152px;top:320px;width:32px;height:30px;border-radius:50% 0 50% 0;background:linear-gradient(135deg,#f2c35a,#c9791f)}
.wheel{position:absolute;left:14px;top:368px;width:130px;height:150px}
.success{position:absolute;left:141px;top:361px}
.success h3{font-size:8px;font-weight:500;line-height:10px}
.success h3 span{display:block;margin-left:25px;color:var(--ochre)}
.success ul{list-style:none;margin-top:6px}
.success li{position:relative;font-size:6.3px;line-height:7px;font-weight:500;padding-left:11px;margin-bottom:13px;min-height:7px}
.success li::before{content:"";position:absolute;left:-1px;top:0;width:5px;height:6px;border-radius:50% 0;background:var(--ochre)}

/* partners panel */
.partners{text-align:center;padding-top:30px}
.partners .our{font-size:26px;color:var(--ink);margin-left:20px}
.partners .big{font-size:44px;color:var(--gum);margin-top:-8px}
.partners .tag{font-size:10px;margin-top:8px;color:var(--ink);letter-spacing:.2px}
.logo-grid{display:grid;grid-template-columns:repeat(3,1fr);row-gap:34px;column-gap:6px;padding:40px 18px 0}
.logo{display:flex;flex-direction:column;align-items:center;gap:4px;font-size:5.6px;font-weight:600;color:var(--ink);line-height:7px}
.logo i{display:block;width:22px;height:22px;border-radius:50%;background:var(--plain-mark)}
.logo i.sq{border-radius:2px}
.logo-row-last{display:flex;justify-content:center;gap:26px;margin-top:28px}
.dev{display:flex;align-items:center;gap:6px;justify-content:center;margin-top:38px;font-size:7.6px;font-weight:500;letter-spacing:.4px;color:var(--ink)}
.dev::before,.dev::after{content:"";width:16px;height:.8px;background:var(--ink)}
.ref{display:flex;align-items:center;gap:10px;justify-content:center;margin-top:26px;color:var(--ink);text-align:left}
.ref i{width:48px;height:48px;border-radius:6px;background:var(--plain-mark)}
.ref span{font-size:10px;line-height:12px}
.ref small{font-size:7px;letter-spacing:.6px}

/* cover */
.cover .eyebrow{position:absolute;left:20px;top:47px;font-size:10px;letter-spacing:.4px}
.cover .title{position:absolute;left:53px;top:73px;font-size:30px}
.cover .title-big{position:absolute;left:20px;top:95px;font-size:47px;color:var(--ochre)}
.wattle{position:absolute;left:34px;top:150px;width:200px;height:290px;background:radial-gradient(ellipse at 55% 50%,#f2c35a 0%,#d48a2a 40%,rgba(29,59,61,0) 72%)}
.cover .strap{position:absolute;left:24px;top:469px;font-size:11px;line-height:17px;letter-spacing:.2px}
.cover .strap b{font-weight:600;color:var(--ochre)}

/* inside principles */
.principle{position:absolute;left:0;width:100%}
.principle--top{top:0;height:246px}
.principle--bottom{top:246px;height:295px}
.panel--gum{background:var(--gum)}
.panel--paper{background:var(--white);color:var(--ink)}
.panel--paper .accent{color:var(--ochre-deep)}
.ghost-label{position:absolute;right:13px;top:11px;font-size:10px;line-height:10px;font-weight:600;color:rgba(255,255,255,.35);letter-spacing:.2px}
.panel--paper .ghost-label{color:#b8b8b8;right:18px}
.principle--bottom .ghost-label{top:0}
.bar{position:absolute;left:0;right:0;top:21px;height:20px;background:var(--night);color:var(--white);display:flex;align-items:center;padding-left:12px;font-size:6.6px;font-weight:500;gap:6px}
.bar .accent{color:var(--ochre)}
.principle--bottom .bar{top:10px}
.bar .icon{width:10px;height:10px;border:1.2px solid var(--white);border-radius:2px}
.bar .leaf{width:4px;height:6px;border-radius:50% 0;background:var(--ochre)}
.copy{position:absolute;left:12px;right:9px;top:51px;font-size:6.3px;line-height:9.6px;font-weight:400}
.panel--paper .copy{left:5px}
.principle--bottom .copy{top:40px}
.copy ul{list-style:none;padding-left:4px}
.copy li{position:relative;padding-left:6px}
.copy li::before{content:"•";position:absolute;left:0}
.copy .gap{margin-top:9.6px}
</style>
</head>
<body>

<section class="spread spread--outside">
  <article class="panel panel--night">
    <div class="intro">
      <p class="eyebrow" style="margin:0">Shared Guidelines for</p>
      <h1 class="serif title">Community</h1>
      <div class="serif title-big">Renewal</div>
      <p style="margin-top:9px">Disasters can deeply impact lives and livelihoods. Working with communities recovering from disasters is complex and challenging. These principles are a way to guide our efforts, our approach, our planning, and our decision-making.</p>
      <p>Disaster recovery is part of emergency management, which includes the broader components of prevention, preparedness, and response. Planning for recovery is integral to emergency preparation, and mitigation actions may often be initiated as part of recovery.</p>
      <p>Disaster recovery includes built, environmental, and economic elements, all contributing to individual and social wellbeing.</p>
      <p>Recovery can provide an opportunity to improve these aspects beyond previous conditions, contributing to a more resilient community.</p>
      <p class="subhead">THE RELATIONSHIP BETWEEN THE PRINCIPLES</p>
      <p>While all the principles are equally critical to ensure effective recovery, understanding the local and broader <span class="accent">context</span> and recognizing <span class="accent">complexity</span> are foundational.</p>
      <p>The descriptions beneath each principle (overleaf) provide further guidance for working with communities in disaster recovery.</p>
      <p>ISBN: 000-0-00000-000-0 (PDF/Online)</p>
    </div>
    <div class="sprig" role="img" aria-label="Small wattle sprig"></div>
    <svg class="wheel" viewBox="0 0 130 150" role="img" aria-label="Recovery at the centre, surrounded by the six principles">
      <defs>
        <path id="inner-ring" d="M25 80 A40 40 0 1 1 105 80 A40 40 0 1 1 25 80"/>
      </defs>
      <path d="M20 54 A52 52 0 0 1 110 54" fill="none" stroke="#2a4d4f" stroke-width="14"/>
      <path d="M20 106 A52 52 0 0 0 110 106" fill="none" stroke="#2a4d4f" stroke-width="14"/>
      <circle cx="65" cy="80" r="33" fill="#2f6b62"/>
      <text x="65" y="82.5" text-anchor="middle" font-family="Poppins,sans-serif" font-size="6.4" fill="#fff">RECOVERY</text>
      <text x="65" y="33" text-anchor="middle" font-family="Poppins,sans-serif" font-size="6.2" fill="#fff">CONTEXT</text>
      <text x="65" y="133" text-anchor="middle" font-family="Poppins,sans-serif" font-size="6.2" fill="#fff">COMPLEXITY</text>
      <g font-family="Poppins,sans-serif" font-size="5.4" fill="#e9a23b">
        <text><textPath href="#inner-ring" startOffset="5%">CAPACITY</textPath></text>
        <text><textPath href="#inner-ring" startOffset="28%">COORDINATE</textPath></text>
        <text><textPath href="#inner-ring" startOffset="54%">COMMUNICATE</textPath></text>
        <text><textPath href="#inner-ring" startOffset="77%">COMMUNITY-LED</textPath></text>
      </g>
    </svg>
    <div class="success">
      <h3>SUCCESSFUL<span>RECOVERY</span></h3>
      <ul>
        <li>Understand the <span class="accent">CONTEXT</span></li>
        <li>Recognise <span class="accent">COMPLEXITY</span></li>
        <li style="margin-bottom:10px">Use <span class="accent">COMMUNITY-LED</span><br>approaches</li>
        <li><span class="accent">COORDINATE</span> all activities</li>
        <li><span class="accent">COMMUNICATE</span> effectively</li>
        <li>Recognise and build<br><span class="accent">CAPACITY</span></li>
      </ul>
    </div>
  </article>

  <article class="panel panel--sand partners">
    <div class="serif our">Our</div>
    <div class="serif big">Partners</div>
    <p class="tag">Working together across Australia</p>
    <div class="logo-grid">
      <div class="logo"><i></i>Federal Dept of<br>Community Services</div>
      <div class="logo"><i></i>Capital Region<br>Council</div>
      <div class="logo"><i></i>Federal Dept of<br>Civic Affairs</div>
      <div class="logo"><i></i>Southern Aid<br>Network</div>
      <div class="logo"><i></i>Southern State<br>Office</div>
      <div class="logo"><i></i>Northern Coast<br>Office</div>
      <div class="logo"><i></i>Western State<br>Office</div>
      <div class="logo"><i class="sq"></i>Bayside State<br>Office</div>
      <div class="logo"><i></i>Island State<br>Office</div>
    </div>
    <div class="logo-row-last">
      <div class="logo"><i></i>Top End Office</div>
      <div class="logo"><i class="sq"></i>Eastern Office<br>of Recovery</div>
    </div>
    <p class="dev">PARTNERS IN DEVELOPMENT FROM THE</p>
    <div class="ref"><i></i><span>Community Renewal<br>Reference Circle<br><small>AUSTRALIA</small></span></div>
  </article>

  <article class="panel panel--night cover">
    <p class="eyebrow">Shared Guidelines for</p>
    <h2 class="serif title">Community</h2>
    <div class="serif title-big">Renewal</div>
    <div class="wattle" role="img" aria-label="Large illustrated golden wattle branch"></div>
    <p class="strap">WORKING TOGETHER TO HELP<br>COMMUNITIES <b>RECOVER FROM<br>DISASTER</b></p>
  </article>
</section>

<section class="spread spread--inside">
  <div class="panel">
    <article class="principle principle--top panel--gum">
      <span class="ghost-label">CONTEXT</span>
      <div class="bar"><span class="icon"></span><span class="leaf"></span>Understand the <span class="accent">CONTEXT</span></div>
      <div class="copy">
        <p>Successful recovery is based on an understanding of the community context, with each community having its own history, values and dynamics.</p>
        <p>Recovery should:</p>
        <ul>
          <li>Acknowledge existing strengths and capacity, including past experiences;</li>
          <li>Appreciate the risks and stressors faced by the community;</li>
          <li>Be respectful of and sensitive to the culture and diversity of the community;</li>
          <li>Support those who may be facing vulnerability;</li>
          <li>Recognise the importance of the environment to people and to their recovery;</li>
          <li>Be acknowledged as requiring a long term sustained effort as needed by the community; and</li>
          <li>Acknowledge that the impact upon the community may extend beyond the geographical boundaries where the disaster occurred.</li>
        </ul>
      </div>
    </article>
    <article class="principle principle--bottom panel--gum">
      <span class="ghost-label">COMPLEXITY</span>
      <div class="bar"><span class="icon"></span><span class="leaf"></span>Recognise <span class="accent">COMPLEXITY</span></div>
      <div class="copy">
        <p>Successful recovery is responsive to the complex and dynamic nature of both emergencies and the community.</p>
        <p class="gap">Recovery should recognise that:</p>
        <p class="gap">* Disasters lead to a range of effects and impacts that require a variety of approaches; they can also leave long-term legacies;</p>
        <p>* Information on impacts is limited at first and changes over time;</p>
        <p>* Affected individuals and the community have diverse needs, wants and expectations, which can evolve rapidly;</p>
        <p>* Responsive and flexible action is crucial to address immediate needs;</p>
        <p>* Existing community knowledge and values may challenge the assumptions of those outside of the community;</p>
        <p>* Conflicting knowledge, values and priorities among individuals, the community and organisations may create tensions;</p>
        <p>* Emergencies create stressful environments where grief or blame may also affect those involved; and</p>
        <p>* Over time, appropriate support for individuals and communities, from within and outside, can cultivate hope and individual and collective growth.</p>
      </div>
    </article>
  </div>

  <div class="panel">
    <article class="principle principle--top panel--paper">
      <span class="ghost-label">COMMUNITY-LED</span>
      <div class="bar"><span class="icon"></span><span class="leaf"></span>Use <span class="accent">COMMUNITY-LED</span> approaches</div>
      <div class="copy">
        <p>Successful recovery is community-centred, responsive and flexible, engaging with community and supporting them to move forward.</p>
        <p>Recovery should:</p>
        <ul>
          <li>Assist and enable individuals, families and the community to actively participate in their own recovery;</li>
          <li>Recognise that individuals and the community may need different levels of support at different times;</li>
          <li>Be guided by the community’s priorities;</li>
          <li>Channel effort through pre-identified and existing community assets, including local knowledge, existing community strengths and resilience;</li>
          <li>Build collaborative partnerships between the community and those involved in the recovery process;</li>
          <li>Recognise that new community leaders often emerge during and after a disaster, who may not hold formal positions of authority; and</li>
          <li>Recognise that different communities may choose different paths to recovery.</li>
        </ul>
      </div>
    </article>
    <article class="principle principle--bottom panel--paper">
      <span class="ghost-label">COORDINATE</span>
      <div class="bar"><span class="icon"></span><span class="leaf"></span><span class="accent">COORDINATE</span> all activities</div>
      <div class="copy">
        <p>Successful recovery requires a planned, coordinated and adaptive approach, between community and partner agencies, based on continuing assessment of impacts and need.</p>
        <p>Recovery should:</p>
        <ul>
          <li>Have clearly articulated and shared goals based on desired outcomes;</li>
          <li>Be flexible, taking into account changes in community needs or stakeholder expectations;</li>
          <li>Be guided by those with experience and expertise, using skilled, authentic and capable community leadership;</li>
          <li>Be at the pace desired by the community, and seek to collaborate and reconcile different interests and time frames;</li>
          <li>Reflect well-developed community planning and information gathering before, during and after a disaster;</li>
          <li>Have clear decision-making and reporting structures and sound governance, which are transparent and accessible to the community;</li>
          <li>Demonstrate an understanding of the roles, responsibilities and authority of organisations involved and coordinate across agencies to ensure minimal service provision disruption;</li>
          <li>Be part of an emergency management approach that integrates with response operations and contributes to future prevention and preparedness; and</li>
          <li>Be inclusive, availing of and building upon relationships created before, during and after the emergency.</li>
        </ul>
      </div>
    </article>
  </div>

  <div class="panel">
    <article class="principle principle--top panel--gum">
      <span class="ghost-label">COMMUNICATE</span>
      <div class="bar"><span class="icon"></span><span class="leaf"></span><span class="accent">COMMUNICATE</span> effectively</div>
      <div class="copy" style="top:55px">
        <p>Successful recovery is built on effective communication between the affected community and other partners.</p>
        <p>Recovery should:</p>
        <ul>
          <li>Recognise that communication should be two-way, and that input and feedback should be encouraged;</li>
          <li>Ensure that information is accessible to audiences in diverse situations, addresses a variety of communication needs, and is provided through a range of media and networks;</li>
          <li>Establish mechanisms for coordinated and consistent communications between all service providers, organisations and individuals and the community;</li>
          <li>Ensure that all communication is relevant, timely, clear, accurate, targeted, credible and consistent; and</li>
          <li>Identify trusted sources of information and repeat key recovery messages to enable greater community confidence and receptivity.</li>
        </ul>
      </div>
    </article>
    <article class="principle principle--bottom panel--gum">
      <span class="ghost-label">CAPACITY</span>
      <div class="bar"><span class="icon"></span><span class="leaf"></span>Recognise and build <span class="accent">CAPACITY</span></div>
      <div class="copy">
        <p>Successful recovery recognises, supports and builds on individual, community and organisational capacity and resilience.</p>
        <p>Recovery should:</p>
        <ul>
          <li>Assess capability and capacity requirements before, during and after a disaster;</li>
          <li>Support the development of self-reliance, preparation and disaster mitigation;</li>
          <li>Quickly identify and mobilise community skills, strengths and resources;</li>
          <li>Develop networks and partnerships to strengthen capacity, capability and resilience;</li>
          <li>Provide opportunities to share, transfer and develop knowledge, skills and training;</li>
          <li>Recognise that resources can be provided by a range of partners and from community networks;</li>
          <li>Acknowledge that existing resources may be stretched, and that additional resources may be sought;</li>
          <li>Understand that additional resources may only be available for a limited period, and that sustainability may need to be addressed;</li>
          <li>Understand when and how to step back, while continuing to support individuals and the community as a whole to be more self-sufficient when they are ready; and</li>
          <li>Be evaluated to provide learning for future and improved resilience.</li>
        </ul>
      </div>
    </article>
  </div>
</section>

</body>
</html>
```